LedgaVue Business Card

We need a business card design using the attached logo. The company is a financial services company that provides a dashboard (chart based information) for Executives of small businesses to use to better manage their information. The design must be progressive, make good utilization of the logo and project stability and financial security.

Industry/Entity Type

Financial

```html
<!DOCTYPE html>
<html lang="en">
<head>
<meta charset="utf-8">
<title>LedgaVue Business Card</title>
<link rel="stylesheet" href="https://fonts.googleapis.com/css2?family=Mulish:wght@400;700&display=swap">
<style>
  :root {
    --page-bg: #f4f4f4;
    --card-white: #ffffff;
    --card-black: #121212;
    --card-black-soft: #1e1e1e;
    --brand-red: #b3161b;
    --ink: #222222;
    --ink-light: #f2f2f2;
  }
  * { box-sizing: border-box; margin: 0; padding: 0; }
  html, body {
    width: 1200px;
    height: 900px;
    overflow: hidden;
    background: var(--page-bg);
    font-family: "Mulish", "Century Gothic", sans-serif;
  }
  .stage {
    position: relative;
    width: 1200px;
    height: 900px;
    display: flex;
    align-items: center;
    justify-content: center;
    gap: 56px;
  }
  .card {
    position: relative;
    width: 520px;
    height: 298px;
    border-radius: 24px;
    overflow: hidden;
    box-shadow: 0 10px 28px rgba(0,0,0,0.18);
  }

  /* Front */
  .card-front { background: var(--card-white); }
  .front-top {
    position: absolute;
    inset: 0 0 auto 0;
    height: 148px;
    background: linear-gradient(180deg, #ffffff 0%, #f1f1f1 100%);
  }
  .brand {
    position: absolute;
    left: 26px;
    top: 62px;
    display: flex;
    align-items: center;
    gap: 12px;
  }
  .brand-square {
    width: 40px;
    height: 40px;
    background: var(--brand-red);
  }
  .brand-name {
    font-size: 44px;
    font-weight: 700;
    color: var(--ink);
    letter-spacing: -0.5px;
  }
  .holder {
    position: absolute;
    right: 30px;
    top: 22px;
    text-align: right;
  }
  .holder-name {
    font-size: 20px;
    font-weight: 700;
    color: var(--brand-red);
  }
  .holder-title {
    font-size: 15px;
    font-weight: 700;
    color: var(--ink);
    margin-top: 2px;
  }
  .front-stripe {
    position: absolute;
    left: 0; right: 0;
    top: 148px;
    height: 12px;
    background: var(--brand-red);
  }
  .front-bottom {
    position: absolute;
    left: 0; right: 0;
    top: 160px;
    bottom: 0;
    background: linear-gradient(180deg, var(--card-black-soft) 0%, var(--card-black) 100%);
    padding: 14px 22px;
  }
  .contact-list { list-style: none; }
  .contact-item {
    display: flex;
    align-items: flex-start;
    gap: 8px;
    color: var(--ink-light);
    font-size: 15px;
    line-height: 20px;
  }
  .contact-icon {
    width: 14px;
    height: 14px;
    margin-top: 3px;
    flex: none;
    fill: var(--brand-red);
  }
  .contact-icon.spacer { visibility: hidden; }

  /* Back */
  .card-back {
    background: radial-gradient(ellipse at center, #2a2a2a 0%, var(--card-black) 70%);
    display: flex;
    align-items: center;
    justify-content: center;
    gap: 16px;
  }
  .back-square {
    width: 56px;
    height: 56px;
    background: var(--brand-red);
  }
  .back-name {
    font-size: 58px;
    font-weight: 700;
    color: var(--ink-light);
    letter-spacing: -0.5px;
  }
</style>
</head>
<body>
<main class="stage">
  <section class="card card-front" aria-label="Business card front">
    <div class="front-top">
      <div class="brand">
        <span class="brand-square"></span>
        <span class="brand-name">LedgaVue</span>
      </div>
      <div class="holder">
        <p class="holder-name">Dana Whitfield</p>
        <p class="holder-title">Manager</p>
      </div>
    </div>
    <div class="front-stripe"></div>
    <div class="front-bottom">
      <ul class="contact-list">
        <li class="contact-item">
          <svg class="contact-icon" viewBox="0 0 16 16" aria-hidden="true"><path d="M3 1l3 3-1.5 2a9 9 0 0 0 5.5 5.5L12 10l3 3-2 2C7 15 1 9 1 3z"/></svg>
          <span>555-214-8830</span>
        </li>
        <li class="contact-item">
          <svg class="contact-icon" viewBox="0 0 16 16" aria-hidden="true"><rect x="2" y="6" width="12" height="8" rx="1"/><rect x="4" y="1" width="8" height="4"/></svg>
          <span>555-214-8831</span>
        </li>
        <li class="contact-item">
          <svg class="contact-icon" viewBox="0 0 16 16" aria-hidden="true"><path d="M8 1l7 7h-2v7H10v-4H6v4H3V8H1z"/></svg>
          <span>4180 Meridan</span>
        </li>
        <li class="contact-item">
          <svg class="contact-icon spacer" viewBox="0 0 16 16" aria-hidden="true"></svg>
          <span>Fairview, TX 75001</span>
        </li>
        <li class="contact-item">
          <svg class="contact-icon" viewBox="0 0 16 16" aria-hidden="true"><path d="M1 4h14v9H1z M1 4l7 5 7-5" stroke="#121212" stroke-width="1"/></svg>
          <span>d.whitfield@ledgavue.com</span>
        </li>
      </ul>
    </div>
  </section>

  <section class="card card-back" aria-label="Business card back">
    <span class="back-square"></span>
    <span class="back-name">LedgaVue</span>
  </section>
</main>
</body>
</html>
```